WordPress Site Clean up

We are a small wireless networking company in Norther Colorado. We have a basic layout to our new website, and require a person or persons who can clean the new site up so we can go live with it in the coming weeks. Our company has the logo and content, we just need to clean the formatting up, improve the colors/graphics. It is currently a PLIXORA. We also need help making our project pictures look better on the website, and clean up the images all around.

The website can be found at: www.7kqairgrid.com/newsite

We can provide you with photos and more content, but we have gone as far as we can with "building" the wordpress site.

It Company

```html
<!DOCTYPE html>
<html lang="en">
<head>
<meta charset="utf-8">
<title>Tarnwell Networks</title>
<link href="https://fonts.googleapis.com/css2?family=Open+Sans:wght@400;600&family=Roboto:wght@400&family=Lato:wght@400&display=swap" rel="stylesheet">
<style>
  :root {
    --green: #7cbb43;
    --ink: #333333;
    --body: #555555;
    --rule: #e4e4e4;
    --band: #f0f0f0;
    --white: #ffffff;
    --arrow-bg: #1c1c1c;
  }
  * { box-sizing: border-box; margin: 0; padding: 0; }
  html, body { width: 1200px; height: 900px; overflow: hidden; background: var(--white); }
  body { font-family: "Open Sans", sans-serif; color: var(--body); position: relative; }

  .top-bar { height: 6px; background: var(--green); }

  .site-header { height: 96px; position: relative; border-bottom: 1px solid var(--rule); }
  .brand {
    position: absolute; left: 106px; top: 34px;
    font-family: "Open Sans", sans-serif; font-weight: 600; font-size: 24px;
    color: var(--ink); letter-spacing: -0.3px; line-height: 30px; white-space: nowrap;
  }
  .main-nav { position: absolute; right: 76px; top: 25px; display: flex; }
  .main-nav a {
    display: block; height: 48px; line-height: 48px; padding: 0 12px;
    font-size: 14px; color: var(--ink); text-decoration: none; text-transform: uppercase; white-space: nowrap;
  }
  .main-nav a.is-active { background: var(--green); color: var(--white); padding: 0 14px; }

  .hero { position: absolute; top: 103px; left: 0; width: 1200px; height: 425px; }
  .hero-photo {
    width: 100%; height: 100%;
    background: linear-gradient(100deg, #4f7fc9 0%, #6e98d8 35%, #8db3e6 55%, #c9761f 70%, #6b7fb0 100%);
  }
  .slider-arrow {
    position: absolute; top: 184px; width: 40px; height: 53px;
    background: var(--arrow-bg); display: flex; align-items: center; justify-content: center;
  }
  .slider-arrow.prev { left: 2px; }
  .slider-arrow.next { right: 2px; }

  .features { position: absolute; top: 598px; left: 0; width: 1200px; }
  .feature { position: absolute; width: 310px; text-align: center; }
  .feature-icon {
    width: 45px; height: 45px; margin: 0 auto; border: 1px solid var(--ink); border-radius: 50%;
    display: flex; align-items: center; justify-content: center;
  }
  .feature.is-highlight .feature-icon { border-color: var(--green); }
  .feature h2 {
    font-family: "Roboto", sans-serif; font-weight: 400; font-size: 19px;
    color: var(--ink); margin-top: 16px; line-height: 24px;
  }
  .feature.is-highlight h2 { color: var(--green); }
  .feature p { font-family: "Lato", sans-serif; font-size: 13px; line-height: 20px; margin-top: 8px; }

  .what-we-do { position: absolute; top: 818px; left: 0; width: 1200px; height: 82px; background: var(--band); }
  .what-we-do h2 {
    position: absolute; left: 458px; top: 46px;
    font-weight: 400; font-size: 33px; color: var(--green); line-height: 40px; white-space: nowrap;
  }
</style>
</head>
<body>
  <div class="top-bar"></div>

  <header class="site-header">
    <div class="brand">Tarnwell Networks</div>
    <nav class="main-nav">
      <a href="#">Home</a>
      <a href="#">About TWN</a>
      <a href="#" class="is-active">Markets</a>
      <a href="#">Services</a>
      <a href="#">Products</a>
      <a href="#">Success Stories</a>
      <a href="#">Technologies</a>
      <a href="#">Contact</a>
    </nav>
  </header>

  <section class="hero">
    <div class="hero-photo" role="img" aria-label="Two engineers in hard hats and safety vests reviewing plans beside a steel building frame under a blue sky"></div>
    <div class="slider-arrow prev">
      <svg width="16" height="30" viewBox="0 0 16 30"><polyline points="14,2 2,15 14,28" fill="none" stroke="#fff" stroke-width="1.6"/></svg>
    </div>
    <div class="slider-arrow next">
      <svg width="16" height="30" viewBox="0 0 16 30"><polyline points="2,2 14,15 2,28" fill="none" stroke="#fff" stroke-width="1.6"/></svg>
    </div>
  </section>

  <section class="features">
    <div class="feature" style="left:62px">
      <div class="feature-icon">
        <svg width="20" height="16" viewBox="0 0 20 16"><rect x="4" y="2" width="12" height="9" fill="none" stroke="#222" stroke-width="1.6"/><rect x="1" y="12" width="18" height="2" fill="#222"/></svg>
      </div>
      <h2>Services</h2>
      <p>Providing world class services is Tarnwell Network's commitment. We provide a whole host of services from installation to design work.</p>
    </div>
    <div class="feature is-highlight" style="left:410px">
      <div class="feature-icon">
        <svg width="20" height="18" viewBox="0 0 20 18"><path d="M5 1h10v5a5 5 0 0 1-10 0z" fill="#7cbb43"/><path d="M5 3H2v2a3 3 0 0 0 3 3M15 3h3v2a3 3 0 0 1-3 3" fill="none" stroke="#7cbb43" stroke-width="1.4"/><rect x="9" y="10" width="2" height="4" fill="#7cbb43"/><rect x="6" y="14" width="8" height="2.5" fill="#7cbb43"/></svg>
      </div>
      <h2>Solutions</h2>
      <p>We are a vendor neutral solution provider. We carefully learn the needs of our customers and fit them with the right solution.</p>
    </div>
    <div class="feature" style="left:757px">
      <div class="feature-icon">
        <svg width="22" height="20" viewBox="0 0 22 20"><circle cx="8" cy="12" r="5" fill="none" stroke="#222" stroke-width="3" stroke-dasharray="2.2 1.7"/><circle cx="8" cy="12" r="1.6" fill="#222"/><circle cx="16" cy="5" r="3.4" fill="none" stroke="#222" stroke-width="2.4" stroke-dasharray="1.6 1.3"/><circle cx="16" cy="5" r="1" fill="#222"/></svg>
      </div>
      <h2>Design</h2>
      <p>Designing networks is a combination of science, standards and a little bit of art. Many IT companies can sell you the equipment, but we not only sell it, we understand it, and will guarantee it will work.</p>
    </div>
  </section>

  <section class="what-we-do">
    <h2>WHAT WE DO</h2>
  </section>
</body>
</html>
```